Veteran Reserved Parking Sign 12x18

Brave Hearts Kinship Network is looking to have a new Veteran Reserved Parking Sign designed. Included in the files are our current logo, the rectangle with the name on it. Also included is our Alt Square version that we will often use. There are several other signs that we kind of like as examples, not not asking for exactly like those, we want you to be creative and show us some new ideas. These are full sized parking signs, 12" wide X 18" height.

Target Market(s)

Veterans and Military Friendly Americans

Industry/Entity Type

Veteran Nonprofit

Font styles to use
Other font styles liked:
• Our logo uses the Franklin Heavy Gothic Font but you are not required to use that font in design.

Requirements
Must have
• Our logo needs to be on there and well as BHKN.ORG
Should not have
• CAN NOT Mention Steadfast Soldier Alliance or have black silhouettes similar to their logo. BHKN is NOT the same nonprofit.

```html
<!DOCTYPE html>
<html lang="en">
<head>
<meta charset="utf-8">
<title>Reserved Parking – Veterans Only</title>
<link rel="stylesheet" href="https://fonts.googleapis.com/css2?family=Cinzel:wght@400;700&family=Montserrat:wght@700&display=swap">
<style>
  :root {
    --navy: #082650;
    --red: #b01f3c;
    --white: #ffffff;
  }
  * { margin: 0; padding: 0; box-sizing: border-box; }
  html, body { width: 871px; height: 1200px; overflow: hidden; background: var(--white); }
  .sign { position: relative; width: 871px; height: 1200px; }
  .sign-frame { position: absolute; inset: 0; }
  .banner-title {
    position: absolute; left: 174px; width: 512px; top: 88px;
    text-align: center; color: var(--white);
    font-family: "Cinzel", serif; font-weight: 400; text-transform: uppercase;
    font-size: 70px; line-height: 71px; letter-spacing: 0;
    white-space: nowrap;
  }
  .salute-figure {
    position: absolute; left: 233px; top: 332px; width: 176px; height: 309px;
    background: var(--navy); border-radius: 40px 40px 6px 6px;
  }
  .approved-icon { position: absolute; left: 453px; top: 429px; }
  .restriction {
    position: absolute; left: 93px; width: 685px; top: 700px;
    text-align: center; color: var(--white);
    font-family: "Cinzel", serif; font-weight: 400; text-transform: uppercase;
    font-size: 96px; line-height: 93px; letter-spacing: 0;
    white-space: nowrap;
  }
  .org-mark {
    position: absolute; left: 217px; top: 944px; width: 436px;
    display: flex; align-items: center; gap: 12px;
  }
  .org-mark-square { width: 123px; height: 69px; background: var(--navy); flex: none; }
  .org-mark-name {
    color: var(--red); font-family: "Cinzel", serif; font-weight: 700;
    font-size: 84px; line-height: 69px; letter-spacing: 2px;
  }
  .org-full-name {
    position: absolute; left: 217px; width: 436px; top: 1022px;
    text-align: center; color: var(--red);
    font-family: "Cinzel", serif; font-weight: 700; font-size: 22px;
    white-space: nowrap;
  }
  .org-web {
    position: absolute; left: 0; width: 871px; top: 1064px;
    text-align: center; color: var(--navy);
    font-family: "Montserrat", sans-serif; font-weight: 700;
    font-size: 36px; letter-spacing: 1px;
  }
</style>
</head>
<body>
<main class="sign">
  <svg class="sign-frame" width="871" height="1200" viewBox="0 0 871 1200" aria-hidden="true">
    <rect x="60" y="40" width="752" height="1122" rx="69" fill="var(--navy)"/>
    <rect x="78" y="58" width="716" height="1086" rx="52" fill="var(--white)"/>
    <rect x="89" y="69" width="694" height="1064" rx="42" fill="none" stroke="var(--red)" stroke-width="9"/>
    <rect x="166" y="60" width="540" height="20" fill="var(--white)"/>
    <polygon points="174,58 686,58 686,209 430,312 174,209" fill="var(--navy)"/>
    <polygon points="174,219 430,311 686,219 686,228 430,316 174,228" fill="var(--red)"/>
    <polygon points="174,239 430,316 686,239 686,247 430,320 174,247" fill="var(--red)"/>
    <rect x="93" y="669" width="685" height="241" fill="var(--red)"/>
  </svg>

  <h1 class="banner-title">Reserved<br>Parking</h1>

  <div class="salute-figure" role="img" aria-label="Pictogram of a uniformed veteran saluting"></div>

  <svg class="approved-icon" width="160" height="160" viewBox="0 0 160 160" role="img" aria-label="Approved tick">
    <circle cx="80" cy="80" r="70" fill="none" stroke="var(--navy)" stroke-width="13"/>
    <polyline points="48,82 70,104 114,58" fill="none" stroke="var(--navy)" stroke-width="14" stroke-linecap="round" stroke-linejoin="round"/>
  </svg>

  <p class="restriction">Veterans<br>Only</p>

  <div class="org-mark">
    <span class="org-mark-square"></span>
    <span class="org-mark-name">BHKN</span>
  </div>
  <p class="org-full-name">Brave Hearts Kinship Network</p>
  <p class="org-web">BHKN.ORG</p>
</main>
</body>
</html>
```